Psychic / Tarot Reader needs updated Facebook Page

We need a new design for our Facebook page.
Logo is attached and copy of new website that is being launched.
We need something fresh, simple and eye catching

current Facebook: MoonWillowGlow

layout for entire Facebook please

Target Market(s)

18 +

Requirements
Must have
• colours
• easy to use
• services

```html
<!DOCTYPE html>
<html lang="en">
<head>
<meta charset="utf-8">
<title>MoonWillowGlow – Psychic, Healer &amp; Tarot Card Reader</title>
<link href="https://fonts.googleapis.com/css2?family=Arimo:wght@700&display=swap" rel="stylesheet">
<style>
  :root {
    --sky-top: #e2ecbd;
    --sky-mid: #eef3d6;
    --sky-haze: #f6f8ea;
    --floor-light: #d2b084;
    --floor-mid: #b88e5f;
    --floor-dark: #9a7047;
    --ink: #111111;
    --brand-purple: #8b2a8c;
    --card-deep: #2b3b9a;
    --card-mid: #4a6ad0;
    --card-glow: #7fa3ea;
  }

  * { margin: 0; padding: 0; box-sizing: border-box; }

  html, body {
    width: 1200px;
    height: 451px;
    overflow: hidden;
  }

  .cover {
    position: relative;
    width: 1200px;
    height: 451px;
    overflow: hidden;
    font-family: "Arimo", Arial, sans-serif;
    background:
      radial-gradient(ellipse 520px 200px at 620px 300px, var(--sky-haze) 0%, rgba(246,248,234,0) 100%),
      linear-gradient(180deg, var(--sky-top) 0%, var(--sky-mid) 60%, var(--sky-haze) 100%);
  }

  .wood-floor {
    position: absolute;
    left: 0;
    top: 322px;
    width: 1200px;
    height: 129px;
    background:
      linear-gradient(180deg, rgba(238,240,220,0.85) 0%, rgba(238,240,220,0) 35%),
      linear-gradient(180deg, var(--floor-light) 0%, var(--floor-mid) 55%, var(--floor-dark) 100%);
  }

  .brand {
    position: absolute;
    left: 40px;
    top: 58px;
    display: flex;
    align-items: center;
    gap: 10px;
  }

  .brand-dot {
    width: 18px;
    height: 18px;
    border-radius: 50%;
    background: var(--brand-purple);
  }

  .brand-name {
    font-size: 30px;
    font-weight: 700;
    color: var(--brand-purple);
    letter-spacing: 0.2px;
  }

  .headline {
    position: absolute;
    left: 40px;
    top: 228px;
    text-transform: uppercase;
    font-weight: 700;
  }

  .headline-lead {
    display: block;
    font-size: 28px;
    line-height: 34px;
    color: var(--ink);
  }

  .headline-services {
    display: block;
    font-size: 37px;
    line-height: 43px;
    color: var(--brand-purple);
    letter-spacing: 0.3px;
  }

  .tarot-cards {
    position: absolute;
    left: 768px;
    top: 54px;
    width: 392px;
    height: 334px;
    border-radius: 14px;
    background:
      radial-gradient(ellipse 140px 120px at 62% 52%, var(--card-glow) 0%, rgba(127,163,234,0) 100%),
      linear-gradient(135deg, var(--card-mid) 0%, var(--card-deep) 100%);
    transform: rotate(-3deg);
  }
</style>
</head>
<body>
  <main class="cover">
    <div class="wood-floor" role="img" aria-label="Wooden floorboards in warm tan tones"></div>

    <div class="brand">
      <span class="brand-dot"></span>
      <span class="brand-name">MoonWillowGlow</span>
    </div>

    <h1 class="headline">
      <span class="headline-lead">We are</span>
      <span class="headline-services">A Phychic, Healer &amp;</span>
      <span class="headline-services">Tarot Card&nbsp; Reader Company</span>
    </h1>

    <div class="tarot-cards" role="img" aria-label="Three fanned tarot cards with iridescent blue and violet backs"></div>
  </main>
</body>
</html>
```